Design for a Note buying company that attracts landlords and seller financed notes

I need a card designed. I want a simple clean front with my logo and contact info. On the back I want some big and bold words to get a message across.

Our Company buys Notes (mortgages) and we want to convey the sense of financial security. Our number one market that we pursue is tired landlords.

If you want to understand our business you can visit our website. www.lakeviewpaperfund.com

Do not use any Clip Art in the design, it will not be accepted. I want a custom designed card not something I could throw together myself. Simple clean and drive the message home.

Target Market(s)

Landlords, seller financed note holders

Industry/Entity Type

Mortgage

Contact Information for Business Card

Simple clean and bold. I need to grab the attention of the customer. It should convey a professional touch.

Font styles to use
Sans Serif

Colors
ec2229
ffffff

Requirements
Must have
• Clean front with logo and contact information
Front colors should match logo

Back should be bold and grab attention. Back colors are open to ideas
Nice to have
• The Back May use the phrase "No more Tentants, No more Toilets" "More Time, More Cash"

I'm open to other ideas about grabbing a landlords attention

I'm open to a square card design
I like cards with round corners as well
Should not have
• any clip art! must be custom designs.

```html
<!DOCTYPE html>
<html lang="en">
<head>
<meta charset="utf-8">
<title>Lakeview Paper Fund – Business Card</title>
<link rel="stylesheet" href="https://fonts.googleapis.com/css2?family=Exo+2:wght@400;600;800&family=Open+Sans:wght@400&display=swap">
<style>
  :root {
    --brand-red: #ec2229;
    --ink: #0b0b0b;
    --paper: #ffffff;
    --backdrop: #3b3b3d;
    --muted: #d9d9d9;
  }
  * { box-sizing: border-box; margin: 0; padding: 0; }
  html, body { width: 1200px; height: 900px; overflow: hidden; }
  body {
    background: var(--backdrop);
    font-family: "Exo 2", sans-serif;
    position: relative;
  }
  .card {
    position: absolute;
    left: 232px;
    width: 735px;
    height: 420px;
    border-radius: 30px;
    overflow: hidden;
    background: var(--paper);
    box-shadow: 0 10px 30px rgba(0,0,0,0.45);
  }
  .card--contact { top: 20px; }
  .card--brand { top: 460px; }
  .card-shapes { position: absolute; inset: 0; width: 100%; height: 100%; }

  .wordmark {
    position: absolute;
    display: flex;
    align-items: center;
    gap: 12px;
    color: var(--ink);
    font-weight: 800;
    text-transform: uppercase;
    letter-spacing: 0.04em;
    white-space: nowrap;
  }
  .wordmark-square {
    display: block;
    background: var(--brand-red);
  }
  .card--contact .wordmark { left: 70px; top: 82px; font-size: 30px; }
  .card--contact .wordmark-square { width: 22px; height: 22px; }
  .card--brand .wordmark { left: 50%; top: 120px; transform: translateX(-50%); font-size: 40px; }
  .card--brand .wordmark-square { width: 30px; height: 30px; }

  .holder {
    position: absolute;
    right: 40px;
    top: 195px;
    text-align: right;
  }
  .holder-name {
    color: var(--brand-red);
    font-size: 22px;
    font-weight: 600;
    letter-spacing: 0.18em;
    text-transform: uppercase;
  }
  .holder-title {
    color: var(--paper);
    font-family: "Open Sans", sans-serif;
    font-size: 14px;
    margin-top: 4px;
  }

  .contact-list {
    position: absolute;
    left: 40px;
    top: 292px;
    list-style: none;
  }
  .contact-item {
    display: flex;
    align-items: center;
    gap: 14px;
    height: 29px;
    color: var(--paper);
    font-size: 13px;
    letter-spacing: 0.16em;
    text-transform: uppercase;
  }
  .contact-icon { width: 22px; height: 22px; flex: none; }
</style>
</head>
<body>

<section class="card card--contact" aria-label="Card front with contact details">
  <svg class="card-shapes" viewBox="0 0 735 420" aria-hidden="true">
    <polygon points="0,272 330,272 382,178 735,178 735,420 0,420" fill="var(--ink)"/>
    <line x1="0" y1="258" x2="300" y2="258" stroke="var(--brand-red)" stroke-width="3"/>
    <line x1="420" y1="164" x2="735" y2="164" stroke="var(--brand-red)" stroke-width="3"/>
  </svg>

  <div class="wordmark"><span class="wordmark-square"></span>Lakeview Paper Fund</div>

  <div class="holder">
    <p class="holder-name">Dana Whitfield</p>
    <p class="holder-title">CEO/Managing Director</p>
  </div>

  <ul class="contact-list">
    <li class="contact-item">
      <svg class="contact-icon" viewBox="0 0 22 22" aria-hidden="true">
        <circle cx="11" cy="11" r="10" fill="none" stroke="var(--brand-red)" stroke-width="1.5"/>
        <rect x="8" y="5.5" width="6" height="11" rx="1" fill="none" stroke="var(--brand-red)" stroke-width="1.4"/>
        <line x1="10" y1="14.5" x2="12" y2="14.5" stroke="var(--brand-red)" stroke-width="1.2"/>
      </svg>555-014-2288</li>
    <li class="contact-item">
      <svg class="contact-icon" viewBox="0 0 22 22" aria-hidden="true">
        <circle cx="11" cy="11" r="10" fill="none" stroke="var(--brand-red)" stroke-width="1.5"/>
        <path d="M5.5 11.5 L11 6 L16.5 11.5 M7.5 10 V16 H14.5 V10" fill="none" stroke="var(--brand-red)" stroke-width="1.4"/>
      </svg>555-014-2288</li>
    <li class="contact-item">
      <svg class="contact-icon" viewBox="0 0 22 22" aria-hidden="true">
        <circle cx="11" cy="11" r="10" fill="none" stroke="var(--brand-red)" stroke-width="1.5"/>
        <rect x="6" y="7.5" width="10" height="7" fill="none" stroke="var(--brand-red)" stroke-width="1.4"/>
        <path d="M6 7.5 L11 11.5 L16 7.5" fill="none" stroke="var(--brand-red)" stroke-width="1.2"/>
      </svg>dana@lakeviewpaperfund.com</li>
    <li class="contact-item">
      <svg class="contact-icon" viewBox="0 0 22 22" aria-hidden="true">
        <circle cx="11" cy="11" r="10" fill="none" stroke="var(--brand-red)" stroke-width="1.5"/>
        <circle cx="11" cy="11" r="5.5" fill="none" stroke="var(--brand-red)" stroke-width="1.2"/>
        <ellipse cx="11" cy="11" rx="2.3" ry="5.5" fill="none" stroke="var(--brand-red)" stroke-width="1"/>
        <line x1="5.5" y1="11" x2="16.5" y2="11" stroke="var(--brand-red)" stroke-width="1"/>
      </svg>www.lakeviewpaperfund.com</li>
  </ul>
</section>

<section class="card card--brand" aria-label="Card back with company name">
  <svg class="card-shapes" viewBox="0 0 735 420" aria-hidden="true">
    <polygon points="0,388 420,388 446,322 735,322 735,420 0,420" fill="var(--ink)"/>
    <polyline points="0,374 410,374 436,308 735,308" fill="none" stroke="var(--brand-red)" stroke-width="3"/>
  </svg>

  <div class="wordmark"><span class="wordmark-square"></span>Lakeview Paper Fund</div>
</section>

</body>
</html>
```